Life Coaching and Career Coaching company needs new website with bold, modern, videos

We need a whole new website that is heavy on video. We are a small company who sells personal wellbeing services like career coaching, life coaching, and group coaching programs. The programs all help people design a better life.
FULL BRIEF ATTACHED and STYLE GUIDE
Also, look at https://www.brightfennel.com/coaching and galdrove.com and https://www.marnwick.life/ for a small amount of inspiration.

Industry/Entity Type

personal well-being/life coaching/career coaching

Number of Pages Required

3 page

Other font styles liked:
• fonts are in the brief

Requirements
Must have
• read the brief please - it's all in there. (things like the look, feel, how it will have lots of video, etc,)
Nice to have
• something really different looking and breakthrough. visually stunning. very trustworthy. Please read the brief, its all in there.
Should not have
• should not look like other life coaching websites. must have video!

```html
<!DOCTYPE html>
<html lang="en">
<head>
<meta charset="utf-8">
<title>Orvel Coaching — Life &amp; Career Coaching</title>
<link href="https://fonts.googleapis.com/css2?family=Righteous&family=Montserrat:wght@300;400;500;600;700&display=swap" rel="stylesheet">
<style>
:root{
  --coral:#F0605D;
  --ink:#333335;
  --text:#8a8a8a;
  --pink-band:#FDEFEF;
  --pink-blob:#FCE3E3;
  --dark:#3B3B3D;
  --grey-shadow:#E4E4E6;
  --white:#ffffff;
}
*{box-sizing:border-box;margin:0;padding:0}
html,body{width:1200px;height:4713px;overflow:hidden}
body{position:relative;background:var(--white);font-family:"Montserrat",sans-serif;color:var(--ink)}
.abs{position:absolute}
.display{font-family:"Righteous",sans-serif;font-weight:400;text-transform:uppercase;letter-spacing:1px}
.body-copy{font-size:13px;line-height:20px;color:var(--text);font-weight:400}
.btn{position:absolute;display:flex;align-items:center;justify-content:center;border-radius:30px;font-size:10px;font-weight:700;text-transform:uppercase;letter-spacing:.3px}
.btn-coral{background:var(--coral);color:var(--white);box-shadow:0 6px 14px rgba(240,96,93,.3)}
.photo{position:absolute;overflow:hidden}
.hero-bg{position:absolute;left:0;top:0;width:1200px;height:800px}

.nav{left:88px;top:33px;width:1022px;height:84px;background:var(--white);border-radius:8px;box-shadow:0 10px 30px rgba(0,0,0,.08);display:flex;align-items:center;padding:0 28px}
.brand{display:flex;align-items:center;gap:10px}
.brand-dot{width:14px;height:14px;border-radius:50%;background:var(--coral)}
.brand-name{font-family:"Montserrat",sans-serif;font-weight:500;font-size:26px;color:#555;letter-spacing:.5px}
.menu{display:flex;gap:18px;margin-left:auto;font-size:11.5px;font-weight:600;color:#444;align-items:center}
.menu svg{display:block}
.signin{margin-left:26px;width:104px;height:40px;border:2px solid var(--coral);border-radius:22px;color:var(--coral);font-size:10px;font-weight:700;display:flex;align-items:center;justify-content:center}

.welcome{left:88px;top:246px;font-size:32px;color:var(--white)}
.hero-mark{left:84px;top:300px;font-size:128px;color:var(--white);letter-spacing:4px;line-height:1}
.hero-copy{left:88px;top:462px;width:400px;font-size:14px;line-height:21px;color:var(--white);font-weight:400}
.btn-white{background:var(--white);color:var(--ink)}
.btn-ghost{border:2px solid var(--white);color:var(--white)}
.scroll-btn{left:552px;top:810px;width:96px;height:96px;border-radius:50%;background:var(--white);box-shadow:0 8px 24px rgba(0,0,0,.1);display:flex;align-items:center;justify-content:center}
.play{position:absolute;border-radius:50%;background:var(--coral);display:flex;align-items:center;justify-content:center;box-shadow:0 10px 26px rgba(240,96,93,.35)}

.band{left:0;top:1953px;width:1200px;height:598px;background:var(--pink-band)}
.step{position:absolute;top:1719px;width:243px;height:375px;border-radius:122px;background:var(--white);box-shadow:0 14px 34px rgba(0,0,0,.09);text-align:center;padding-top:58px}
.step-num{font-size:11px;font-weight:700;color:var(--coral);margin-top:14px}
.step-title{font-size:21px;color:var(--ink);line-height:25px;margin-top:6px}
.step-copy{font-size:12.5px;line-height:20px;color:var(--text);margin:14px auto 0;width:190px}

.faq{position:absolute;left:216px;width:768px;height:56px;border-radius:28px;background:var(--white);box-shadow:0 6px 22px rgba(0,0,0,.08);display:flex;align-items:center;padding:0 30px}
.faq-q{font-family:"Righteous",sans-serif;font-size:16px;text-transform:uppercase;color:var(--ink);letter-spacing:.4px}
.faq-sign{margin-left:auto;color:var(--coral);font-size:16px}
.faq-open{position:absolute;left:216px;top:3018px;width:768px;height:174px;background:var(--white);border-left:3px solid var(--coral);border-radius:4px;box-shadow:0 6px 22px rgba(0,0,0,.08);padding:26px 30px}

.dot{position:absolute;border-radius:50%;border:4px solid var(--white);box-shadow:0 6px 18px rgba(0,0,0,.15);overflow:hidden}

.cta{left:172px;top:4000px;width:856px;height:185px;border-radius:93px;background:var(--coral);box-shadow:6px 8px 0 var(--white),8px 12px 0 rgba(0,0,0,.12)}
.foot-h{position:absolute;top:4398px;font-family:"Righteous",sans-serif;font-size:19px;color:var(--white);text-transform:uppercase}
.foot-list{position:absolute;top:4446px;list-style:none;font-size:11px;color:#cfcfcf;text-transform:uppercase;line-height:27px}
.social{position:absolute;top:4453px;width:36px;height:36px;border-radius:50%;border:1.5px solid #777}
</style>
</head>
<body>

<svg class="hero-bg" viewBox="0 0 1200 800" aria-hidden="true">
  <path d="M0 0 H985 C960 120 880 200 800 280 C700 420 640 620 560 690 C470 760 360 720 250 680 C150 640 70 640 0 655 Z" fill="var(--grey-shadow)" transform="translate(0 22)"/>
  <path d="M0 0 H985 C960 120 880 200 800 280 C700 420 640 620 560 690 C470 760 360 720 250 680 C150 640 70 640 0 655 Z" fill="var(--coral)"/>
</svg>

<nav class="abs nav">
  <div class="brand"><span class="brand-dot"></span><span class="brand-name">ORVEL COACHING</span></div>
  <div class="menu">
    <span>JOBS ⌄</span><span>COMPANIES</span><span>ADVICE</span><span>COACHING</span><span>EMPLOYERS</span>
    <svg width="16" height="16" viewBox="0 0 16 16" fill="none" stroke="#444" stroke-width="1.6"><circle cx="8" cy="5" r="3.5"/><path d="M2 15c0-3.3 2.7-5 6-5s6 1.7 6 5"/></svg>
    <svg width="16" height="16" viewBox="0 0 16 16" fill="none" stroke="#444" stroke-width="1.8"><circle cx="7" cy="7" r="5"/><path d="M11 11l4 4"/></svg>
  </div>
  <div class="signin">SIGN IN</div>
</nav>

<div class="abs display welcome">Welcome to</div>
<div class="abs display hero-mark">Orvel</div>
<p class="abs hero-copy">It is a long established fact that a reader will be distracted by the readable content of a page when looking at its layout</p>
<div class="btn btn-white" style="left:88px;top:540px;width:152px;height:40px">See our services</div>
<div class="btn btn-ghost" style="left:248px;top:540px;width:122px;height:40px">Learn more</div>

<div class="photo" role="img" aria-label="Photo: laptop and coloured folders on an office desk" style="left:572px;top:229px;width:288px;height:466px;border-radius:144px 144px 0 0;background:linear-gradient(160deg,#f4f4f4,#dcdcdc)"></div>
<svg class="abs" style="left:862px;top:256px" width="300" height="530" viewBox="0 0 300 530" fill="none" aria-hidden="true">
  <path d="M16 140 A137 137 0 0 1 290 140 V380 A137 137 0 0 1 16 380 Z" stroke="var(--coral)" stroke-width="3"/>
</svg>
<div class="photo" role="img" aria-label="Photo: smiling young businesswoman working at a laptop" style="left:868px;top:240px;width:270px;height:520px;border-radius:135px;background:linear-gradient(170deg,#efefef,#cfcfcf 55%,#2b2b2b);box-shadow:0 12px 30px rgba(0,0,0,.12)"></div>

<div class="abs scroll-btn"><svg width="20" height="12" viewBox="0 0 20 12" fill="none" stroke="var(--ink)" stroke-width="2.4"><path d="M2 2l8 8 8-8"/></svg></div>

<div class="photo" role="img" aria-label="Photo: coach in a grey blazer presenting with a tablet" style="left:119px;top:977px;width:504px;height:504px;border-radius:50%;background:linear-gradient(135deg,#f1f1f1,#c9c9c9)"></div>
<div class="play" style="left:488px;top:1344px;width:132px;height:132px"><svg width="26" height="28" viewBox="0 0 26 28"><path d="M2 2l22 12L2 26z" fill="#fff"/></svg></div>
<h2 class="abs display" style="left:699px;top:1052px;font-size:36px">About Orvel</h2>
<p class="abs body-copy" style="left:699px;top:1112px;width:370px;line-height:20.5px">It is a long established fact that a reader will be distracted by the readable content of a page when looking at its layout. The point of using Lorem Ipsum is that it has a more-or-less normal distribution of letters, as opposed to using 'Content here, content here', making it look like readable English. Many desktop publishing packages and web page editors now use Lorem Ipsum as their default model text, and a search for 'lorem ipsum' will uncover many web sites still in their infancy. Various versions have evolved over the years,</p>
<div class="btn btn-coral" style="left:699px;top:1357px;width:126px;height:38px">Read more</div>

<h2 class="abs display" style="left:0;width:1200px;top:1568px;text-align:center;font-size:38px">How it works</h2>
<p class="abs body-copy" style="left:220px;width:760px;top:1628px;text-align:center">It is a long established fact that a reader will be distracted by the readable content of a page when looking at its layout. The point of using Lorem Ipsum is that it has</p>
<div class="abs band"></div>

<div class="step" style="left:88px">
  <svg width="64" height="64" viewBox="0 0 64 64" fill="none" stroke="var(--coral)" stroke-width="2.2"><rect x="6" y="6" width="24" height="24" rx="3"/><rect x="36" y="6" width="22" height="22" rx="3"/><rect x="6" y="36" width="22" height="22" rx="3"/><path d="M38 40l14 4-6 3 6 6-3 3-6-6-3 6z"/></svg>
  <div class="step-num">STEP 01</div><div class="step-title display">Choose<br>a service</div>
  <p class="step-copy">It is a long established fact that a reader will be distracted by the readable content of a page when looking at its layout.</p>
</div>
<div class="step" style="left:349px">
  <svg width="64" height="64" viewBox="0 0 64 64" fill="none" stroke="var(--coral)" stroke-width="2.2"><circle cx="36" cy="10" r="5"/><path d="M36 16v18l-8 10M36 34l8 10M28 24h16M6 58h14V48h14V38h14V28h10"/></svg>
  <div class="step-num">STEP 02</div><div class="step-title display">Book a<br>career coach</div>
  <p class="step-copy">It is a long established fact that a reader will be distracted by the readable content of a page when looking at its layout.</p>
</div>
<div class="step" style="left:608px">
  <svg width="64" height="64" viewBox="0 0 64 64" fill="none" stroke="var(--coral)" stroke-width="2.2"><path d="M32 4l8 8h-5v14h14v-5l8 8-8 8v-5H35v14h5l-8 8-8-8h5V35H15v5l-8-8 8-8v5h14V12h-5z"/></svg>
  <div class="step-num">STEP 03</div><div class="step-title display">Decide<br>on a time</div>
  <p class="step-copy">It is a long established fact that a reader will be distracted by the readable content of a page when looking at its layout.</p>
</div>
<div class="step" style="left:867px">
  <svg width="64" height="64" viewBox="0 0 64 64" fill="none" stroke="var(--coral)" stroke-width="2.2"><path d="M56 8c-14 0-26 8-32 22l10 10c14-6 22-18 22-32z"/><circle cx="42" cy="22" r="4"/><path d="M24 30l-10 2-6 8 12 0M34 40l-2 10-8 6 0-12M18 46l-8 10"/></svg>
  <div class="step-num">STEP 04</div><div class="step-title display">Get<br>started!</div>
  <p class="step-copy">It is a long established fact that a reader will be distracted by the readable content of a page when looking at its layout.</p>
</div>

<h2 class="abs display" style="left:159px;top:2248px;font-size:38px;line-height:44px">Denmark's<br>leading experts</h2>
<p class="abs body-copy" style="left:159px;top:2346px;width:390px">It is a long established fact that a reader will be distracted by the readable content of a page when looking at its layout. The point of using Lorem Ipsum is that it has a more-or-less normal distribution of letters, as opposed to using 'Content here.</p>
<div class="btn btn-coral" style="left:159px;top:2463px;width:142px;height:38px">Explore more</div>
<div class="photo" role="img" aria-label="Photo: diverse group of smiling friends huddled together" style="left:611px;top:2171px;width:432px;height:432px;border-radius:50%;background:linear-gradient(135deg,#d9d2c8,#8f8579 60%,#4a4440)"></div>
<div class="play" style="left:598px;top:2482px;width:96px;height:96px"><svg width="18" height="20" viewBox="0 0 18 20"><path d="M2 2l14 8-14 8z" fill="#fff"/></svg></div>

<h2 class="abs display" style="left:0;width:1200px;top:2660px;text-align:center;font-size:38px;text-transform:none">FAQs</h2>
<div class="faq" style="top:2730px"><span class="faq-q">Why are some coaches more expensive than others?</span><span class="faq-sign">+</span></div>
<div class="faq" style="top:2800px"><span class="faq-q">I've never done anything like this what should I expect?</span><span class="faq-sign">+</span></div>
<div class="faq" style="top:2869px"><span class="faq-q">How long does it take to start working with the coach?</span><span class="faq-sign">+</span></div>
<div class="faq" style="top:2937px"><span class="faq-q">Which coach/service do I need?</span><span class="faq-sign">+</span></div>
<div class="faq-open">
  <div style="display:flex"><span class="faq-q">What if I do not want to finish my package?</span><span class="faq-sign" style="margin-left:auto">–</span></div>
  <p class="body-copy" style="margin-top:16px;font-size:12.5px">If a cancellation request is made when a package is partially completed, we will issue a refund for only the sessions which have not started (pre-coaching assessment is starting point). Individual sessions will not be refunded following the first call. Packages include the "Fresh Start Search Kit," "Career Reset Package" and "First-Time Lead Program".</p>
</div>
<div class="abs" style="left:0;width:1200px;top:3226px;text-align:center;font-size:11px;font-weight:700;color:var(--coral);text-decoration:underline">VIEW ALL FAQS</div>
<div class="abs" style="left:878px;top:3160px;width:360px;height:360px;border-radius:50%;background:var(--pink-blob);opacity:.7;z-index:-1"></div>

<svg class="abs" style="left:170px;top:3340px" width="260" height="540" viewBox="0 0 260 540" fill="none" aria-hidden="true">
  <path d="M190 20 C40 120 0 230 12 300 C22 390 90 470 185 520" stroke="var(--coral)" stroke-width="1.5" stroke-dasharray="6 6"/>
</svg>
<div class="photo" role="img" aria-label="Photo: reviewer in a coral blazer" style="left:294px;top:3458px;width:308px;height:308px;border-radius:50%;background:linear-gradient(160deg,#f0ecea,#e9857c 70%,#d75c55)"></div>
<div class="dot" role="img" aria-label="Photo: reviewer portrait" style="left:301px;top:3297px;width:112px;height:112px;background:linear-gradient(135deg,#f2ece6,#b7a89d)"></div>
<div class="dot" role="img" aria-label="Photo: reviewer portrait" style="left:149px;top:3452px;width:112px;height:112px;background:linear-gradient(135deg,#eae6e2,#8b7a6e)"></div>
<div class="dot" role="img" aria-label="Photo: reviewer portrait" style="left:149px;top:3670px;width:112px;height:112px;background:linear-gradient(135deg,#e8ebf0,#3e4a66)"></div>
<div class="dot" role="img" aria-label="Photo: reviewer portrait" style="left:297px;top:3801px;width:112px;height:112px;background:linear-gradient(135deg,#f3f0ed,#c9b8a8)"></div>

<h2 class="abs" style="left:671px;top:3442px;font-size:36px;text-transform:uppercase;font-family:'Montserrat',sans-serif;font-weight:500">Customer reviews</h2>
<p class="abs body-copy" style="left:671px;top:3490px;width:390px;line-height:20.5px">It is a long established fact that a reader will be distracted by the readable content of a page when looking at its layout. The point of using Lorem Ipsum is that it has a more-or-less normal distribution of letters, as opposed to using 'Content here, content here', making it look like readable English. Many desktop publishing packages and web page editors now use Lorem Ipsum as their default model text, and a search for 'lorem ipsum' will uncover many web sites still in their infancy.</p>
<div class="abs" style="left:671px;top:3706px;font-size:14px;color:var(--coral);font-weight:500">Jana Holt</div>
<svg class="abs" style="left:671px;top:3731px" width="82" height="16" viewBox="0 0 82 16" aria-label="5 stars">
  <g fill="#F3A73B"><path id="s" d="M8 1l2.1 4.6 5 .5-3.8 3.4 1.1 5L8 12 3.6 14.5l1.1-5L.9 6.1l5-.5z"/><use href="#s" x="16"/><use href="#s" x="32"/><use href="#s" x="48"/><use href="#s" x="64"/></g>
</svg>
<div class="abs" style="left:673px;top:3758px;width:28px;height:28px;border-radius:50%;background:var(--coral);display:flex;align-items:center;justify-content:center"><svg width="8" height="12" viewBox="0 0 8 12" fill="none" stroke="#fff" stroke-width="2"><path d="M6 2L2 6l4 4"/></svg></div>
<div class="abs" style="left:709px;top:3758px;width:28px;height:28px;border-radius:50%;background:var(--ink);display:flex;align-items:center;justify-content:center"><svg width="8" height="12" viewBox="0 0 8 12" fill="none" stroke="#fff" stroke-width="2"><path d="M2 2l4 4-4 4"/></svg></div>

<svg class="abs" style="left:0;top:3900px" width="1200" height="813" viewBox="0 0 1200 813" aria-hidden="true">
  <path d="M900 110 C1000 60 1120 40 1200 30 V260 H880 Z" fill="var(--pink-blob)"/>
  <path d="M0 330 C300 310 700 330 950 250 C1060 215 1140 160 1200 120 V813 H0 Z" fill="var(--dark)"/>
</svg>

<div class="abs cta"></div>
<div class="abs" style="left:246px;top:4040px;font-family:'Montserrat',sans-serif;font-weight:500;font-size:36px;line-height:38px;color:var(--white);text-transform:uppercase">Elevate your<br>professional journey.</div>
<div class="abs" style="left:246px;top:4126px;font-size:11px;font-weight:600;color:var(--white)">Explore Our Coaching Network and Connect with Your Ideal Guide.</div>
<div class="btn btn-white" style="left:756px;top:4069px;width:216px;height:46px;font-size:11px">Browse all coaches</div>

<div class="abs" style="left:0;width:1200px;top:4285px;text-align:center;color:var(--white);font-family:'Montserrat',sans-serif;font-weight:500;font-size:52px;letter-spacing:1px;line-height:1">ORVEL COACHING</div>

<div class="foot-h" style="left:88px">Information</div>
<ul class="foot-list" style="left:88px"><li>Coaching</li><li>Life coaching</li><li>Group coaching programs</li></ul>

<div class="foot-h" style="left:334px">Quick links</div>
<ul class="foot-list" style="left:334px"><li>› Jobs</li><li>› Companies</li><li>› Advice</li><li>› Coaching</li><li>› Employers</li></ul>

<div class="foot-h" style="left:511px">Need help?</div>
<ul class="foot-list" style="left:511px"><li>Try for free</li><li>Customer service</li><li>Membership conditions</li><li>Cookie and privacy policy</li></ul>

<div class="foot-h" style="left:746px">Contact us</div>
<div class="abs" style="left:746px;top:4450px;font-size:11px;color:#cfcfcf;line-height:17px">
  <div style="display:flex;gap:8px"><svg width="12" height="12" viewBox="0 0 12 12"><path d="M3 1l2 3-1 1.5c.7 1.3 1.6 2.2 2.6 2.7L8 7l3 2-1 2C5 11 1 7 1 2z" fill="var(--coral)"/></svg><div>PHONE*<br>+08 123 456 7890</div></div>
  <div style="display:flex;gap:8px;margin-top:20px"><svg width="12" height="12" viewBox="0 0 12 12"><rect x="1" y="2.5" width="10" height="7" rx="1" fill="var(--coral)"/><path d="M1.5 3l4.5 3.5L10.5 3" stroke="#fff" fill="none"/></svg><div>EMAIL*<br>info@example.com</div></div>
  <div style="display:flex;gap:8px;margin-top:20px"><svg width="12" height="14" viewBox="0 0 12 14"><path d="M6 1a4 4 0 0 1 4 4c0 3-4 8-4 8S2 8 2 5a4 4 0 0 1 4-4z" fill="var(--coral)"/><circle cx="6" cy="5" r="1.5" fill="#fff"/></svg><div>LOCATION*<br>Some address line<br>goes here city name</div></div>
</div>

<div class="foot-h" style="left:940px">Follow us</div>
<div class="social" style="left:942px"></div>
<div class="social" style="left:984px"></div>
<div class="social" style="left:1026px"></div>
<div class="social" style="left:1068px"></div>

<div class="abs" style="left:88px;top:4662px;width:1022px;height:1px;background:#5a5a5c"></div>
<div class="abs" style="left:0;width:1200px;top:4682px;text-align:center;font-size:10px;color:#cfcfcf;font-weight:500">© 2022 ORVEL COACHING RIGHTS RESERVED</div>

</body>
</html>
```